Business Card Design Project

We need a business card design for a consultancy called 'Amber Ridge'. The design should communicate innovation and professionalism. The colors used should complement our logo. Please include source files for winning design.
Updates

Industry/Entity Type

Business

Colors

Designer to choose colors to be used in the design.

Requirements
Must have
• Card size should be 85mm x 50mm. The back side of the card should be the logo on a black background. The front side should display the name 'Amber Ridge' along with standard information. The front's design should graphically complement the back.
Nice to have
• Any graphical elements in the front the complement the back side (with the logo on a black background) would be a plus.

```html
<!DOCTYPE html>
<html lang="en">
<head>
<meta charset="utf-8">
<title>Amber Ridge – Business Cards</title>
<link href="https://fonts.googleapis.com/css2?family=Cinzel:wght@500&family=Open+Sans:wght@400;600&display=swap" rel="stylesheet">
<style>
  :root {
    --canvas: #e9e6e1;
    --ink: #0d0d0d;
    --ink-soft: #1f1f1f;
    --paper: #ffffff;
    --amber: #f7941d;
    --amber-deep: #e57c0b;
    --text-light: #f2f2f2;
    --text-dark: #1a1a1a;
  }
  * { box-sizing: border-box; margin: 0; padding: 0; }
  html, body { width: 1200px; height: 784px; overflow: hidden; }
  body {
    background: var(--canvas);
    font-family: "Open Sans", Arial, sans-serif;
    display: flex;
    align-items: center;
    justify-content: center;
    gap: 40px;
  }
  .card {
    width: 560px;
    height: 330px;
    position: relative;
    overflow: hidden;
    box-shadow: 0 6px 18px rgba(0,0,0,0.18);
  }

  /* Back */
  .card-back {
    background: radial-gradient(ellipse at 45% 35%, var(--ink-soft) 0%, var(--ink) 70%);
    display: flex;
    flex-direction: column;
    align-items: center;
    justify-content: center;
    gap: 14px;
  }
  .brand-dot {
    width: 96px; height: 96px;
    border-radius: 50%;
    background: var(--amber);
  }
  .brand-name {
    font-family: "Cinzel", "Times New Roman", serif;
    font-weight: 500;
    color: var(--amber);
    font-size: 30px;
    letter-spacing: 1px;
  }

  /* Front */
  .card-front { background: var(--paper); }
  .front-top {
    position: absolute; left: 0; top: 0;
    width: 100%; height: 168px;
    background: var(--paper);
  }
  .chart-wash {
    position: absolute; right: 0; top: 0;
    width: 250px; height: 168px;
    background: linear-gradient(100deg, rgba(255,255,255,0) 0%, #eef0f1 45%, #e4e6e8 100%);
  }
  .holder {
    position: absolute; right: 22px; top: 14px;
    text-align: right;
  }
  .holder-name { color: var(--amber); font-size: 14px; font-weight: 400; line-height: 1.1; }
  .holder-role { color: var(--text-dark); font-size: 9px; line-height: 1.3; }
  .front-brand {
    position: absolute; left: 0; top: 40px; width: 100%;
    display: flex; flex-direction: column; align-items: center; gap: 8px;
  }
  .front-brand .brand-dot { width: 80px; height: 80px; }
  .front-brand .brand-name { font-size: 24px; }
  .amber-rule {
    position: absolute; left: 0; top: 168px;
    width: 100%; height: 8px;
    background: linear-gradient(90deg, var(--amber-deep), var(--amber));
  }
  .front-bottom {
    position: absolute; left: 0; top: 176px;
    width: 100%; height: 154px;
    background: linear-gradient(180deg, var(--ink-soft), var(--ink));
  }
  .contact-list {
    list-style: none;
    position: absolute; left: 22px; top: 12px;
  }
  .contact-list li {
    display: flex; align-items: center; gap: 6px;
    color: var(--text-light);
    font-size: 13px;
    line-height: 18px;
  }
  .contact-list li.indent { padding-left: 20px; }
  .icon { width: 14px; height: 14px; flex: none; }
  .icon * { fill: var(--amber); }
</style>
</head>
<body>

  <section class="card card-back" aria-label="Card back">
    <div class="brand-dot"></div>
    <div class="brand-name">Amber Ridge</div>
  </section>

  <section class="card card-front" aria-label="Card front">
    <div class="front-top">
      <div class="chart-wash" role="img" aria-label="Faint nautical chart backdrop"></div>
      <div class="holder">
        <div class="holder-name">Dana Whitfield</div>
        <div class="holder-role">Manager</div>
      </div>
      <div class="front-brand">
        <div class="brand-dot"></div>
        <div class="brand-name">Amber Ridge</div>
      </div>
    </div>
    <div class="amber-rule"></div>
    <div class="front-bottom">
      <ul class="contact-list">
        <li>
          <svg class="icon" viewBox="0 0 14 14"><rect x="3" y="0.5" width="8" height="13" rx="1.5"/><rect x="4.3" y="2" width="5.4" height="7.5" fill="#111" style="fill:#111"/></svg>
          555-210-4471
        </li>
        <li>
          <svg class="icon" viewBox="0 0 14 14"><path d="M3 1 L5.5 1 L6.5 4 L5 5.2 C5.8 7 7 8.2 8.8 9 L10 7.5 L13 8.5 L13 11 C13 12 12 13 11 13 C5.5 12.5 1.5 8.5 1 3 C1 2 2 1 3 1 Z"/></svg>
          555-210-4472
        </li>
        <li>
          <svg class="icon" viewBox="0 0 14 14"><rect x="3" y="1" width="8" height="4"/><rect x="1" y="5" width="12" height="6" rx="1"/><rect x="3" y="9" width="8" height="4"/></svg>
          555-210-4473
        </li>
        <li>
          <svg class="icon" viewBox="0 0 14 14"><path d="M1 3 H13 V11 H1 Z M1.8 3.6 L7 7.8 L12.2 3.6 L12.2 4.8 L7 9 L1.8 4.8 Z"/></svg>
          hello@amberridge.com
        </li>
        <li>
          <svg class="icon" viewBox="0 0 14 14"><path d="M7 1 A6 6 0 1 0 7 13 A6 6 0 1 0 7 1 Z M7 2.3 C8 3.5 8.5 5 8.6 6.4 H5.4 C5.5 5 6 3.5 7 2.3 Z M2.4 7.6 H4.2 C4.3 9 4.7 10.4 5.4 11.5 C3.8 10.9 2.7 9.4 2.4 7.6 Z M2.4 6.4 C2.7 4.6 3.8 3.1 5.4 2.5 C4.7 3.6 4.3 5 4.2 6.4 Z M5.4 7.6 H8.6 C8.5 9 8 10.5 7 11.7 C6 10.5 5.5 9 5.4 7.6 Z M9.8 7.6 H11.6 C11.3 9.4 10.2 10.9 8.6 11.5 C9.3 10.4 9.7 9 9.8 7.6 Z M9.8 6.4 C9.7 5 9.3 3.6 8.6 2.5 C10.2 3.1 11.3 4.6 11.6 6.4 Z"/></svg>
          www.amberridge.com
        </li>
        <li>
          <svg class="icon" viewBox="0 0 14 14"><path d="M7 1 L13 6.5 L11.5 6.5 L11.5 13 L8.5 13 L8.5 9 L5.5 9 L5.5 13 L2.5 13 L2.5 6.5 L1 6.5 Z"/></svg>
          4410 N. Cedar Highway,
        </li>
        <li class="indent">Millbrook, CO 80412</li>
      </ul>
    </div>
  </section>

</body>
</html>
```